Counseling Practice Business Card

I need a professional looking business card incorporating my new logo that was just completed. Card needs to incorporate my name and title, description of my specialty, my address, my phone number, my fax number, my email and my website URL. I need to be able to choose design on/with different paper colors and textures.
I do not have a lot of business card ideas so I am open to anything but I want bold,sharp, clear card without additional designs other than my logo (see attached file info). I am open to different color backgrounds or paper colors including black. I do not like traditional brackets around area codes in phone number or dashes between numbers in phone number. Am open to other ways of presenting including periods between numbers as appropriate. I do not know enough to know what I like yet but I want card to coordinate and work together with my logo. My practice emphasizes natural mental health interventions so any use of color (with background paper color or the blue and green in my logo) that elicits nature is nice. In addition to black, any natural brown or wood looking background might be desirable also. Most of the offerings so far look very similar and boring.

Target Market(s)

Potential therapy clients and other professionals

Contact Information for Business Card

Card information:
Gerald P. Whitcombe, Ph.D.
Licensed Clinical Psychologist
Integrative Health Coach
5214 Ambergate Blvd NW
Suite 815
Cedar Hollow, GA 30000
(555) 555-0143 phone
(555) 555-0178 fax
drgeraldwhitcombe@examplemail.net
brightpathwellness.example

Font styles to use
Serif
Sans Serif
Other font styles liked:
• anything that you think looks crisp, clear and easily readable

Requirements
Must have
• Any color used should coordinate with my logo design (see attached files).
• Card should be printed horizontally so top and bottom are longest sides of rectangle.
• Background color or paper color should complement and highlight logo. Do not like a white background. black, grey, brown or any color my logo would blend well with.
Nice to have
• I would like designer to utilize color to highlight letters/name or phone-fax-web symbols.
• Bottom edge of card could be highlighted if appropriate to an idea.
Should not have
• I would NOT want the card to have a pure white background at all.
• No clear cards.
• Cards should be oriented with long sides on bottom and top, NOT sides. DO NOT LIKE THIS THIN TALL ORIENTATION.

```html
<!DOCTYPE html>
<html lang="en">
<head>
<meta charset="utf-8">
<title>BrightPath Wellness – Business Card</title>
<link rel="stylesheet" href="https://fonts.googleapis.com/css2?family=Open+Sans:wght@400;600;700&display=swap">
<style>
  :root {
    --backdrop: #3a3532;
    --card: #141516;
    --card-edge: #1d1f21;
    --brand-blue: #2f7cc0;
    --brand-green: #2f8f4e;
    --text-grey: #c9cbcd;
    --muted-grey: #7d8185;
    --divider: #55595d;
  }
  * { margin: 0; padding: 0; box-sizing: border-box; }
  html, body {
    width: 1200px;
    height: 864px;
    overflow: hidden;
    background: var(--backdrop);
    font-family: "Open Sans", Arial, sans-serif;
  }
  .stage {
    position: relative;
    width: 1200px;
    height: 864px;
  }
  .card {
    position: absolute;
    width: 540px;
    height: 309px;
    background: linear-gradient(160deg, var(--card-edge), var(--card) 60%);
    border-radius: 4px;
    box-shadow: 0 10px 28px rgba(0,0,0,0.45);
    overflow: hidden;
  }
  .card-front { left: 40px; top: 150px; }
  .card-back { left: 620px; top: 406px; }

  .brand-name {
    color: var(--brand-blue);
    font-weight: 600;
    line-height: 1.05;
    letter-spacing: 0.5px;
  }

  /* Front */
  .card-front .brand {
    position: absolute;
    left: 0; right: 0; top: 92px;
    text-align: center;
  }
  .card-front .brand-name { font-size: 44px; }
  .card-front .front-url {
    position: absolute;
    left: 0; right: 0; bottom: 58px;
    text-align: center;
    color: var(--muted-grey);
    font-size: 13px;
    letter-spacing: 3px;
  }

  /* Back */
  .card-back .brand {
    position: absolute;
    left: 26px; top: 108px;
    width: 220px;
  }
  .card-back .brand-name { font-size: 28px; }
  .card-back .divider {
    position: absolute;
    left: 262px; top: 40px;
    width: 1px; height: 230px;
    background: linear-gradient(to bottom, transparent, var(--divider) 20%, var(--divider) 80%, transparent);
  }
  .details {
    position: absolute;
    left: 280px; top: 40px;
    right: 14px;
    color: var(--text-grey);
    font-size: 12.5px;
    line-height: 1.42;
  }
  .person-name {
    color: var(--brand-blue);
    font-weight: 700;
    font-size: 15px;
    text-transform: uppercase;
    letter-spacing: 0.3px;
  }
  .person-title { color: var(--brand-green); font-size: 12.5px; }
  .address { margin-top: 6px; }
  .contact-list { list-style: none; margin-top: 8px; }
  .contact-list li {
    display: flex;
    align-items: center;
    gap: 8px;
    white-space: nowrap;
  }
  .contact-icon {
    width: 12px; height: 12px;
    flex: none;
    fill: var(--brand-blue);
  }
</style>
</head>
<body>
<main class="stage">
  <section class="card card-front" aria-label="Card front">
    <div class="brand">
      <p class="brand-name">BrightPath<br>Wellness</p>
    </div>
    <p class="front-url">www.brightpathwellness.example</p>
  </section>

  <section class="card card-back" aria-label="Card back">
    <div class="brand">
      <p class="brand-name">BrightPath<br>Wellness</p>
    </div>
    <div class="divider"></div>
    <div class="details">
      <p class="person-name">Gerald P. Whitcombe, Ph.D.</p>
      <p class="person-title">Licensed Clinical Psychologist</p>
      <p class="person-title">Integrative Health Coach</p>
      <p class="address">5214 Ambergate Blvd NW<br>Suite 815<br>Cedar Hollow, GA 30000</p>
      <ul class="contact-list">
        <li>
          <svg class="contact-icon" viewBox="0 0 12 12" aria-hidden="true"><path d="M2.5 1h2l1 2.5-1.3 1a6 6 0 0 0 3.3 3.3l1-1.3L11 7.5v2c0 .8-.7 1.5-1.5 1.5A8.5 8.5 0 0 1 1 2.5C1 1.7 1.7 1 2.5 1z"/></svg>
          (555) 555-0143
        </li>
        <li>
          <svg class="contact-icon" viewBox="0 0 12 12" aria-hidden="true"><path d="M3 1h5l1 1v2H3zM1 5h10v5H9V8H3v2H1zM4 9h4v2H4z"/></svg>
          (555) 555-0178
        </li>
        <li>
          <svg class="contact-icon" viewBox="0 0 12 12" aria-hidden="true"><path d="M1 2.5h10v7H1zM1.6 3 6 6.5 10.4 3"/></svg>
          drgeraldwhitcombe@examplemail.net
        </li>
        <li>
          <svg class="contact-icon" viewBox="0 0 12 12" aria-hidden="true"><circle cx="6" cy="6" r="5"/></svg>
          www.brightpathwellness.example
        </li>
      </ul>
    </div>
  </section>
</main>
</body>
</html>
```